依頼概要
■依頼の目的/概要
「ひなげし名品の会」は足利市内の26の店舗がそれぞれの良い所を伸ばそうとする「逸品運動」を中心に共同で事業を行う組織です。
栃木県足利市は国宝霞峰寺、日本遺産千草学舎などの重要な史跡が点在すところから東の京都、北の鎌倉などと言われることがあります。また、霧見川橋、スカイプラザ、森下はるおの故郷など観光などのポイントが多数あります。
※添付ファイルに会員のカタログがあります。

■依頼詳細
「ひなげし名品の会」加盟の店舗は市内の各所に点在しております。そのためそれぞれの店舗の店頭に飾れるような「のぼり旗」のデザインを募集します。
※添付ファイルに地図があります。

■重視する点
【必須項目】
「ひなげし名品の会」という文字表記

のぼり旗という制約のあるデザインの中で名品会らしさ、足利らしさなどを取り込んだものを希望します。通常ののぼり旗の概念を逸脱するものでも結構ですが、予算が必要以上にかかり様なアイデアは採用が難しくなる可能性がございます。

その他何かご不明な点がございましたら、お気軽にご質問下さい。
よろしくお願いいたします。
足利市のイメージキャラクターをのぼりデザインに使用する事は可能です。
ただし「ひなげし名品会」のイメージキャラクターではございませんのでご確認ください。
なお、キャラクター使用許諾につきましては当会にて行います。
添付データとして「まさとき君」のイラストレータデータを添付させていただきますのでこちらを使用願います。
(※当依頼以外でまさとき君の画像当を使用する場合は霜月観光協会の許可が必要ですのでご注意ください。)
名品の会全体会議にてデザインの選定を行う予定です。
そのため直前の3月14日まで受付を延長させていただきます。
より多くの提案をお願いしたいと思います。
■ 選んだ理由

名品の会の会員からのアンケート調査に基づいて決定いたしました。

■ 提案者全員のお礼・コメント

このたびは名品会ののぼりをデザイン頂き誠にありがとうございます。
市内の各所にこのデザインが掲載されお客様に親しまれるように頑張りたいと思います。

```html
<!DOCTYPE html>
<html lang="ja">
<head>
<meta charset="utf-8">
<title>ひなげし名品の会 のぼり旗</title>
<link rel="stylesheet" href="https://fonts.googleapis.com/css2?family=M+PLUS+Rounded+1c:wght@800&family=Shippori+Mincho+B1:wght@800&display=swap">
<style>
  :root {
    --banner-gray: #6f6f70;
    --pattern-gray: #767677;
    --kana-purple: #7b2fa0;
    --kana-outline: #ffffff;
    --title-maroon: #5a1a2c;
    --title-outline: #cfcfd1;
  }
  html, body {
    margin: 0;
    padding: 0;
    width: 1200px;
    height: 3600px;
    overflow: hidden;
    background: var(--banner-gray);
  }
  .nobori {
    position: relative;
    width: 1200px;
    height: 3600px;
    background: var(--banner-gray);
    overflow: hidden;
  }
  .emblem-pattern {
    position: absolute;
    inset: 0;
    background: var(--pattern-gray);
  }
  .title {
    position: absolute;
    inset: 0;
    display: flex;
    flex-direction: column;
    align-items: center;
    padding-top: 70px;
  }
  .title-kana {
    font-family: "M PLUS Rounded 1c", sans-serif;
    font-weight: 800;
    font-size: 240px;
    line-height: 1;
    color: var(--kana-purple);
    writing-mode: vertical-rl;
    text-orientation: upright;
    letter-spacing: -10px;
    -webkit-text-stroke: 14px var(--kana-outline);
    paint-order: stroke fill;
  }
  .title-main {
    font-family: "Shippori Mincho B1", serif;
    font-weight: 800;
    font-size: 600px;
    line-height: 1;
    color: var(--title-maroon);
    writing-mode: vertical-rl;
    text-orientation: upright;
    margin-top: 90px;
    letter-spacing: 20px;
    -webkit-text-stroke: 16px var(--title-outline);
    paint-order: stroke fill;
  }
  .title-suffix {
    font-family: "Shippori Mincho B1", serif;
    font-weight: 800;
    font-size: 340px;
    line-height: 1;
    color: var(--title-maroon);
    writing-mode: vertical-rl;
    text-orientation: upright;
    margin-top: 110px;
    letter-spacing: 30px;
    -webkit-text-stroke: 12px var(--title-outline);
    paint-order: stroke fill;
  }
</style>
</head>
<body>
  <div class="nobori">
    <div class="emblem-pattern" role="img" aria-label="Faint repeating city emblem pattern in two columns"></div>
    <h1 class="title">
      <span class="title-kana">ひなげし</span>
      <span class="title-main">名品</span>
      <span class="title-suffix">の会</span>
    </h1>
  </div>
</body>
</html>
```